Vantrel Web Services

This is a new It services company operating in Perth western Australia

we need a website that is easy to navigate without a cluttered feel to it it should have the following links and pages

About Us
Services
Clients
Contact Us
MY Vantrel (login for clients)

Hi it is a web based IT services company so we would expect customers to come to the website for 2 different purposes the first is to enquire about our services and then as they become customers come to our website to manage their services so whilst they are seperate we want do not want it to look like 2 different websites

hope this helps

Hi to update this we need a home page and templates for sub pages

this is a design brief only and not the coding of the pages or building of the site

```html
<!DOCTYPE html>
<html lang="en">
<head>
<meta charset="utf-8">
<title>Vantrel Web Services</title>
<link href="https://fonts.googleapis.com/css2?family=Orbitron:wght@500;700&family=Open+Sans:ital,wght@0,400;0,600;0,700;1,400&display=swap" rel="stylesheet">
<style>
:root{
  --red:#a3161a;
  --red-dark:#9a1418;
  --blue:#1a9fd6;
  --blue-btn:#17a0d8;
  --navy:#1c3a8c;
  --grey-nav:#8a8a8a;
  --text:#222;
  --muted:#444;
  --hero-a:#6f7f8f;
  --hero-b:#2d4a6e;
}
*{margin:0;padding:0;box-sizing:border-box}
html,body{width:831px;height:1200px;overflow:hidden;background:#fff}
body{position:relative;font-family:"Open Sans",Arial,sans-serif;color:var(--text)}
.abs{position:absolute}

/* header */
.brand{left:130px;top:20px;display:flex;align-items:center;gap:8px}
.brand-dot{width:30px;height:30px;border-radius:50%;background:var(--red)}
.brand-name{font-weight:700;font-size:20px;color:var(--navy);letter-spacing:1px}
.nav{left:321px;top:31px;width:313px;display:flex;justify-content:space-between;font-family:"Orbitron",sans-serif;font-size:7.5px;font-weight:500;letter-spacing:.6px;color:var(--grey-nav);white-space:nowrap}
.nav a{color:inherit;text-decoration:none;padding-bottom:4px}
.nav a.active{color:var(--blue);border-bottom:2px solid var(--blue)}
.signup{left:646px;top:28px;width:55px;height:17px;background:var(--blue-btn);color:#fff;font-family:"Orbitron",sans-serif;font-weight:700;font-size:7.5px;letter-spacing:1px;display:flex;align-items:center;justify-content:center}

/* hero */
.hero{left:0;top:69px;width:831px;height:347px;background:linear-gradient(90deg,var(--hero-a) 0%,#56697e 45%,var(--hero-b) 70%,#223a5c 100%)}
.hero-title{left:130px;top:185px;width:312px;height:66px;background:var(--red);color:#fff;font-weight:700;font-size:17px;line-height:22px;padding:11px 18px}
.hero-cta{left:130px;top:258px;width:124px;height:32px;background:var(--red);color:#fff;font-weight:600;font-size:13px;display:flex;align-items:center;justify-content:center}
.hero-more{left:265px;top:271px;font-size:8.5px;color:#111;display:flex;align-items:center;gap:5px}
.hero-more i{display:inline-block;width:12px;height:9px;background:var(--red)}
.slider-dots{left:677px;top:388px;display:flex;gap:2px}
.slider-dots span{width:7px;height:7px;border-radius:50%;background:#ccc}
.slider-dots span.on{background:#fff;border:2px solid #111}

/* welcome */
.welcome-title{left:0;top:472px;width:831px;text-align:center;font-family:"Orbitron",sans-serif;font-weight:700;font-size:17px;letter-spacing:1.5px;color:var(--blue)}
.welcome-text{left:160px;top:502px;width:511px;text-align:center;font-size:10.5px;line-height:12.5px;color:var(--text)}
.divider{left:130px;width:571px;height:3px;border-top:3px dotted #8fcbe8}

/* services */
.service{width:180px;display:flex;gap:6px}
.service svg{flex:none}
.service h3{font-size:10.5px;font-weight:700;color:#111;margin:-1px 0 4px}
.service p{font-size:8.5px;line-height:12.5px;color:var(--muted)}

/* bottom columns */
.col-title{width:166px;text-align:center;font-size:12.5px;font-weight:600;color:#111}
.col-rule{width:166px;height:3px;border-top:3px dotted #999}
.avatar{left:198px;top:907px;width:55px;height:55px;border-radius:50%;background:radial-gradient(circle at 50% 40%,#c9d6e0,#7f95aa)}
.quote{left:142px;width:166px;text-align:center;font-size:8.5px;line-height:12.5px;color:var(--muted)}
.quote-mark{left:142px;width:166px;text-align:center;font-size:11px;line-height:11px;font-style:italic;color:#111}
.reviewer{left:142px;top:1060px;width:166px;text-align:center;font-style:italic;font-size:10px;color:var(--blue)}
.view-all{left:142px;top:1088px;width:166px;text-align:center;font-size:7px;color:var(--red)}
.map{left:332px;top:900px;width:166px;height:169px;background:linear-gradient(135deg,#cfe1f2 0%,#e9ecd9 45%,#d6e6f4 100%)}
.map-link{left:332px;top:1088px;width:166px;text-align:center;font-size:7px;color:var(--blue)}
.field{left:521px;width:167px;border:1px solid #ddd;font-size:8.5px;color:#555;padding:7px 9px}
.send{left:521px;top:1075px;width:167px;height:23px;background:var(--blue-btn);color:#fff;font-weight:600;font-size:10.5px;display:flex;align-items:center;justify-content:center}

/* footer */
.footer{left:0;top:1171px;width:831px;height:29px;background:var(--red-dark);color:#fff;font-size:7.5px}
.footer-nav{left:130px;top:10px;display:flex;gap:9px}
.footer-legal{left:515px;top:10px;display:flex;gap:6px;align-items:center}
.footer-legal .social{width:8px;height:8px;border-radius:50%;background:#fff;display:inline-block;margin-left:4px}
</style>
</head>
<body>

<header>
  <div class="abs brand"><span class="brand-dot"></span><span class="brand-name">Vantrel</span></div>
  <nav class="abs nav">
    <a class="active" href="#">ABOUT</a><a href="#">SERVICES</a><a href="#">CLIENTS</a><a href="#">CONTACT</a><a href="#">MY VANTREL</a>
  </nav>
  <div class="abs signup">SIGNUP</div>
</header>

<section>
  <div class="abs hero" role="img" aria-label="Photo of a businessman in a blue shirt and orange tie touching a gear diagram"></div>
  <h1 class="abs hero-title">Vantrel a Web Based Software Development Company...</h1>
  <div class="abs hero-cta">Call to Action</div>
  <div class="abs hero-more">Learn More <i></i></div>
  <div class="abs slider-dots"><span class="on"></span><span></span><span></span></div>
</section>

<section>
  <h2 class="abs welcome-title">WELCOME TO VANTREL</h2>
  <p class="abs welcome-text">Lorem ipsum dolor sit amet, consectetur adipisicing elit, sed do eiusmod tempor incididunt ut labore et dolore magna aliqua. Ut enim ad minim veniam, quis nostrud exercitation ullamco laboris nisi<br>Lorem ipsum dolor sit amet, consectetur adipisicing elit...</p>
  <div class="abs divider" style="top:581px"></div>
</section>

<section>
  <div class="abs service" style="left:130px;top:622px">
    <svg width="27" height="27" viewBox="0 0 27 27"><circle cx="13.5" cy="13.5" r="12.5" fill="#b5b5b5" stroke="#8d8d8d"/><path d="M3 11h21M3 16h21M13.5 1v25" stroke="#d8d8d8" fill="none"/></svg>
    <div><h3>Lorem Ipsum Service</h3><p>Lorem ipsum dolor sit amet, consectetur adipisicing elit, sed do eiusmod tempor</p></div>
  </div>
  <div class="abs service" style="left:326px;top:622px">
    <svg width="35" height="26" viewBox="0 0 35 26"><rect x="1" y="1" width="33" height="24" fill="#fff" stroke="#999" stroke-width="1.5"/><line x1="1" y1="6" x2="34" y2="6" stroke="#999" stroke-width="1.5"/><path d="M13 12l-4 3 4 3M22 12l4 3-4 3M19 11l-3 9" stroke="#888" fill="none"/></svg>
    <div><h3>Lorem Ipsum Service</h3><p>Lorem ipsum dolor sit amet, consectetur adipisicing elit, sed do eiusmod tempor</p></div>
  </div>
  <div class="abs service" style="left:530px;top:622px;width:172px">
    <svg width="42" height="28" viewBox="0 0 42 28"><rect x="6" y="1" width="30" height="21" fill="#fff" stroke="#999" stroke-width="1.5"/><path d="M1 24h40v2H1z" fill="#999"/><path d="M21 7v9M17 9l8 5M25 9l-8 5" stroke="#888"/></svg>
    <div><h3>Lorem Ipsum Service</h3><p>Lorem ipsum dolor sit amet, consectetur adipisicing elit, sed do eiusmod tempor</p></div>
  </div>

  <div class="abs service" style="left:130px;top:715px">
    <svg width="27" height="27" viewBox="0 0 27 27"><circle cx="13.5" cy="13.5" r="12.5" fill="#b5b5b5" stroke="#8d8d8d"/><path d="M3 11h21M3 16h21M13.5 1v25" stroke="#d8d8d8" fill="none"/></svg>
    <div><h3>Lorem Ipsum Service</h3><p>Lorem ipsum dolor sit amet, consectetur adipisicing elit, sed do eiusmod tempor</p></div>
  </div>
  <div class="abs service" style="left:326px;top:715px">
    <svg width="35" height="26" viewBox="0 0 35 26"><rect x="1" y="1" width="33" height="24" fill="#fff" stroke="#999" stroke-width="1.5"/><line x1="1" y1="6" x2="34" y2="6" stroke="#999" stroke-width="1.5"/><path d="M13 12l-4 3 4 3M22 12l4 3-4 3M19 11l-3 9" stroke="#888" fill="none"/></svg>
    <div><h3>Lorem Ipsum Service</h3><p>Lorem ipsum dolor sit amet, consectetur adipisicing elit, sed do eiusmod tempor</p></div>
  </div>
  <div class="abs service" style="left:530px;top:715px;width:172px">
    <svg width="42" height="28" viewBox="0 0 42 28"><rect x="6" y="1" width="30" height="21" fill="#fff" stroke="#999" stroke-width="1.5"/><path d="M1 24h40v2H1z" fill="#999"/><path d="M21 7v9M17 9l8 5M25 9l-8 5" stroke="#888"/></svg>
    <div><h3>Lorem Ipsum Service</h3><p>Lorem ipsum dolor sit amet, consectetur adipisicing elit, sed do eiusmod tempor</p></div>
  </div>
  <div class="abs divider" style="top:816px"></div>
</section>

<section>
  <h4 class="abs col-title" style="left:142px;top:858px">Client Reviews</h4>
  <div class="abs col-rule" style="left:142px;top:885px"></div>
  <div class="abs avatar" role="img" aria-label="Client portrait photo"></div>
  <div class="abs quote-mark" style="top:973px">"</div>
  <p class="abs quote" style="top:985px">Lorem ipsum dolor sit amet, consectetur adipisicing elit, sed do eiusmod incididunt ut labore et dolore magna Lorem ipsum dolor sit amet, consectetu...</p>
  <div class="abs quote-mark" style="top:1041px">"</div>
  <div class="abs reviewer">Dalton</div>
  <div class="abs view-all">View All Reviews</div>

  <h4 class="abs col-title" style="left:332px;top:858px">Atlaso Location</h4>
  <div class="abs col-rule" style="left:332px;top:885px"></div>
  <div class="abs map" role="img" aria-label="Map showing the office location"></div>
  <div class="abs map-link">Enlarge Atlaso Map &#9906;</div>

  <h4 class="abs col-title" style="left:521px;top:858px;width:167px">Get in Touch</h4>
  <div class="abs col-rule" style="left:521px;top:885px;width:167px"></div>
  <div class="abs field" style="top:900px;height:24px">User Name</div>
  <div class="abs field" style="top:927px;height:24px">Email ID</div>
  <div class="abs field" style="top:954px;height:24px">Company</div>
  <div class="abs field" style="top:983px;height:83px">Message</div>
  <div class="abs send">Send Message</div>
</section>

<footer class="abs footer">
  <div class="abs footer-nav"><span>About</span><span>Services</span><span>Clients</span><span>Contact</span><span>MY Vantrel</span></div>
  <div class="abs footer-legal"><span>© Copyright 2014</span><span>-</span><span>Terms and Conditions</span><span class="social"></span><span class="social"></span></div>
</footer>

</body>
</html>
```